Korvix App Graphics Design

Our application promotes location based self expression via pictures and text. The primary focus of the application is on the content posted and not on the person that posted it.

We want a very clean and fresh design that evokes positive energy. Our site is unique so our design should be as well. People will reveal thoughts on our site, so the design should convey a "revealing" feel. Our site is a place where people are comfortable to freely express themselves. Colors we have in mind are blue and green hues with earth tones for background.

Our project is to design ten screens for our Korvix application at resolution of 1136-by-640 pixels:

Feed Screen
Camera Screen
Post Screen
Check In Screen
Approval Screen
Map Screen
Flag Screen
Feed Select Screen
Export Screen
Menu Screen

In the contest phase we will require only three screens to be submitted. The screens we require to be submitted are: Feed Screen; Map Screen and Camera Screen. The designer we select as the winner of the competition will then complete the project and deliver a total of the ten screens described above in the handover phase.

We have attached a document below with detailed specs of each screen, we ask for your innovation to bring these screens to life through your design.
Updates

We want to clarify one aspect regarding the VISOR: the visor needs to be transparent so that when the picture scrolls underneath it, you can still see the picture underneath the visor.

Hi Everyone,

We have noticed that some designers need clarification regarding the visor element in the feed screen.
I have attached two examples to our brief area called:
Visor Example 1 and Visor Example 2

Please note that these are not the style we are looking for but are a good example to the concept of a Transparent Visor above the feed stream. We are looking for you guys to come up with a Visor concept that is consistent with the style of the design you are submitting.

Thanks,

Bo

Target Market(s)

People 17-40 who want to share their thought about the world around them.

Industry/Entity Type

Flag

Font styles to use
Sans Serif
Other font styles liked:
• We like “Helvetica New” or “Avenir” but are flexible

Requirements
Must have
• Visor component should look innovative.

```html
<!DOCTYPE html>
<html lang="en">
<head>
<meta charset="utf-8">
<title>Korvix Camera Screen</title>
<link rel="stylesheet" href="https://fonts.googleapis.com/css2?family=Roboto:wght@700&display=swap">
<style>
  :root {
    --page-bg: #ffffff;
    --accent: #19b6df;
    --button-face: #ffffff;
    --visor: rgba(10, 40, 120, 0.55);
    --strip: rgba(40, 42, 46, 0.78);
    --toolbar: #2a2c30;
    --label: #ffffff;
    --thumb-frame: #ffffff;
  }
  * { margin: 0; padding: 0; box-sizing: border-box; }
  html, body { width: 1200px; height: 1000px; overflow: hidden; background: var(--page-bg); }
  .camera-screen {
    position: absolute; left: 392px; top: 163px;
    width: 423px; height: 744px; overflow: hidden;
    font-family: "Roboto", Arial, sans-serif;
  }
  .viewfinder {
    position: absolute; inset: 0;
    background: linear-gradient(180deg,
      #123a9a 0%, #2a55b8 9%, #8f8a80 13%, #e9e2c9 22%,
      #f0a0cc 38%, #f08a3a 50%, #e87cc4 62%, #ececec 75%,
      #3b3d40 82%, #2b2d30 100%);
  }
  .visor {
    position: absolute; left: 0; top: 0; width: 100%; height: 67px;
    background: var(--visor);
  }
  .round-button {
    position: absolute; width: 38px; height: 38px; border-radius: 50%;
    background: var(--button-face);
    box-shadow: 0 1px 3px rgba(0,0,0,0.35);
    display: flex; align-items: center; justify-content: center;
  }
  .round-button svg { width: 22px; height: 22px; }
  .filter-strip {
    position: absolute; left: 0; top: 607px; width: 100%; height: 75px;
    background: var(--strip);
  }
  .filter-arrow { position: absolute; top: 20px; width: 12px; height: 30px; }
  .filter {
    position: absolute; top: 5px; width: 66px; text-align: center;
  }
  .filter-thumb {
    width: 66px; height: 50px; border: 2px solid var(--thumb-frame);
  }
  .filter-name {
    display: block; margin-top: 1px;
    color: var(--label); font-size: 10px; font-weight: 700;
  }
  .toolbar {
    position: absolute; left: 0; top: 682px; width: 100%; height: 62px;
    background: var(--toolbar);
  }
  .shutter {
    position: absolute; left: 168px; top: 13px; width: 85px; height: 36px;
    border-radius: 18px; background: var(--button-face);
    display: flex; align-items: center; justify-content: center;
    box-shadow: 0 1px 3px rgba(0,0,0,0.35);
  }
  .shutter svg { width: 30px; height: 30px; }
</style>
</head>
<body>
<main class="camera-screen">
  <div class="viewfinder" role="img" aria-label="Live camera view of a colourful street mural on a building wall"></div>

  <div class="visor">
    <div class="round-button" style="left:40px;top:15px" aria-label="Flash">
      <svg viewBox="0 0 24 24"><path d="M14 2 5 14h6l-2 8 9-12h-6z" fill="var(--accent)"/></svg>
    </div>
    <div class="round-button" style="left:93px;top:15px" aria-label="Switch camera">
      <svg viewBox="0 0 24 24"><ellipse cx="12" cy="12" rx="10" ry="5" fill="none" stroke="var(--accent)" stroke-width="2.4"/><rect x="7" y="8" width="10" height="8" rx="2" fill="var(--accent)"/></svg>
    </div>
    <div class="round-button" style="left:286px;top:15px" aria-label="Focus">
      <svg viewBox="0 0 24 24"><circle cx="12" cy="12" r="8" fill="none" stroke="var(--accent)" stroke-width="2"/><path d="M12 2v5M12 17v5M2 12h5M17 12h5" stroke="var(--accent)" stroke-width="2"/></svg>
    </div>
    <div class="round-button" style="left:342px;top:15px" aria-label="Close">
      <svg viewBox="0 0 24 24"><path d="M5 5l14 14M19 5 5 19" stroke="var(--accent)" stroke-width="4.5" stroke-linecap="round"/></svg>
    </div>
  </div>

  <div class="filter-strip">
    <svg class="filter-arrow" style="left:10px" viewBox="0 0 12 30"><path d="M10 2 2 15l8 13" fill="none" stroke="#cfd2d6" stroke-width="2"/></svg>
    <div class="filter" style="left:28px"><div class="filter-thumb" style="background:linear-gradient(135deg,#f06bb8,#f59a2a,#2e6bd8)" role="img" aria-label="Vivid filter preview"></div><span class="filter-name">Vivid</span></div>
    <div class="filter" style="left:102px"><div class="filter-thumb" style="background:linear-gradient(135deg,#eeeeee,#8a8a8a,#2a2a2a)" role="img" aria-label="Ashby filter preview"></div><span class="filter-name">Ashby</span></div>
    <div class="filter" style="left:176px"><div class="filter-thumb" style="background:linear-gradient(135deg,#8c9ae0,#d9b3e8,#4a4f9a)" role="img" aria-label="Instant filter preview"></div><span class="filter-name">Instant</span></div>
    <div class="filter" style="left:250px"><div class="filter-thumb" style="background:linear-gradient(135deg,#ff3fa8,#f0d23a,#c4203a)" role="img" aria-label="Pro filter preview"></div><span class="filter-name">Pro</span></div>
    <div class="filter" style="left:325px"><div class="filter-thumb" style="background:linear-gradient(135deg,#d8c24a,#9a8a2a,#4c4216)" role="img" aria-label="Dorra filter preview"></div><span class="filter-name">Dorra</span></div>
    <svg class="filter-arrow" style="left:397px" viewBox="0 0 12 30"><path d="M2 2l8 13-8 13" fill="none" stroke="#cfd2d6" stroke-width="2"/></svg>
  </div>

  <nav class="toolbar">
    <div class="round-button" style="left:40px;top:12px" aria-label="Gallery">
      <svg viewBox="0 0 24 24"><rect x="7" y="4" width="14" height="12" rx="2" fill="var(--accent)" opacity="0.6"/><rect x="3" y="8" width="14" height="12" rx="2" fill="var(--accent)"/></svg>
    </div>
    <div class="round-button" style="left:93px;top:12px" aria-label="Exposure">
      <svg viewBox="0 0 24 24"><circle cx="12" cy="12" r="5" fill="none" stroke="var(--accent)" stroke-width="2"/><path d="M12 7a5 5 0 0 1 0 10z" fill="var(--accent)"/><path d="M12 1v3M12 20v3M1 12h3M20 12h3M4.2 4.2l2 2M17.8 17.8l2 2M4.2 19.8l2-2M17.8 6.2l2-2" stroke="var(--accent)" stroke-width="2"/></svg>
    </div>
    <div class="shutter" aria-label="Take photo">
      <svg viewBox="0 0 30 30"><circle cx="15" cy="15" r="12" fill="var(--accent)"/><circle cx="15" cy="15" r="5" fill="#ffffff"/><path d="M15 3l3 8M27 15l-8 3M15 27l-3-8M3 15l8-3M23.5 6.5l-6 5.5M23.5 23.5l-5.5-6M6.5 23.5l6-5.5M6.5 6.5l5.5 6" stroke="#ffffff" stroke-width="1.3"/></svg>
    </div>
    <div class="round-button" style="left:286px;top:12px" aria-label="Crop">
      <svg viewBox="0 0 24 24"><path d="M7 2v15h15M2 7h15v15" fill="none" stroke="var(--accent)" stroke-width="3"/></svg>
    </div>
    <div class="round-button" style="left:342px;top:12px" aria-label="Auto enhance">
      <svg viewBox="0 0 24 24"><path d="M4 21 14 11" stroke="var(--accent)" stroke-width="3" stroke-linecap="round"/><path d="M16 3v4M16 13v4M10 9h-4M22 9h-4M12 5l2 2M20 5l-2 2M20 13l-2-2" stroke="var(--accent)" stroke-width="2" stroke-linecap="round"/></svg>
    </div>
  </nav>
</main>
</body>
</html>
```